Author needs a new book, Kindle and Audiobook cover design

I updated and re-edited a book I wrote 25 years ago but now realize the title and design did not get the job done. I am seeking a book, Kindle and audiobook design that will make me stand out. The final design will pop while being sensitive to the nature of the subject. The title of the book is Quiet Lanterns. Subtitle: Ways to Notice and Step Away From Harmful Circles While Keeping Steady Belief by Dorian T. Wexcombe. I am wanting to get the attention of people who have been damaged by a church relationship that started well but ended badly.
Updates

The book title is: Quiet Lanterns. The Subtitle is: Ways To Notice and Step Away From Harmful Circles While Keeping Steady Belief. The dimension is 6x9 (150 pages) and I am the author: Dorian T. Wexcombe

Target Market(s)

People with a church experience; church leadership. Religious abuse victims.

Industry/Entity Type

Christian

Font styles to use
Serif

Colors

Designer to choose colors to be used in the design.

Requirements
Nice to have
• I am not married to the Serif font if another design works better.

```html
<!DOCTYPE html>
<html lang="en">
<head>
<meta charset="UTF-8">
<title>Quiet Lanterns — Book Cover</title>
<link href="https://fonts.googleapis.com/css2?family=Fredoka:wght@600&family=Nunito:wght@600;700&display=swap" rel="stylesheet">
<style>
  :root {
    --page-bg: #e4e4e4;
    --title-ink: #3f4c48;
    --subtitle-ink: #111111;
    --author-ink: #ffffff;
    --sky-top: #b9b9ba;
    --sky-mid: #cfcdca;
    --haze: #e7dfd3;
    --hills-light: #b4b6b6;
    --hills-deep: #868d8c;
    --trees: #3a4636;
    --trees-dark: #252d22;
    --grass-light: #a08c55;
    --grass-dark: #5f5130;
  }
  * { margin: 0; padding: 0; box-sizing: border-box; }
  html, body {
    width: 1200px; height: 1200px; overflow: hidden;
    background: var(--page-bg);
  }
  .canvas {
    width: 1200px; height: 1200px;
    display: flex; align-items: center; justify-content: center;
  }
  .cover {
    position: relative;
    width: 720px; height: 1080px;
    overflow: hidden;
  }
  .cover-scene {
    position: absolute; inset: 0;
    background: linear-gradient(to bottom,
      var(--sky-top) 0%,
      var(--sky-mid) 28%,
      var(--haze) 56%,
      #ddd8cf 70%,
      var(--hills-light) 73%,
      var(--hills-deep) 80%,
      var(--trees) 84%,
      var(--trees-dark) 89%,
      var(--grass-light) 92%,
      var(--grass-dark) 100%);
  }
  .title {
    position: absolute; left: 0; right: 0; top: 78px;
    text-align: center;
    font-family: "Fredoka", sans-serif;
    font-weight: 600;
    color: var(--title-ink);
    text-transform: uppercase;
    line-height: 0.92;
  }
  .title-line-one { display: block; font-size: 150px; letter-spacing: 2px; }
  .title-line-two { display: block; font-size: 104px; letter-spacing: 1px; }
  .subtitle {
    position: absolute; left: 80px; right: 80px; top: 705px;
    text-align: center;
    font-family: "Nunito", sans-serif;
    font-weight: 700;
    font-size: 23px;
    line-height: 1.45;
    color: var(--subtitle-ink);
  }
  .author {
    position: absolute; left: 0; right: 0; bottom: 28px;
    text-align: center;
    font-family: "Nunito", sans-serif;
    font-weight: 700;
    font-size: 36px;
    color: var(--author-ink);
  }
</style>
</head>
<body>
  <main class="canvas">
    <section class="cover">
      <div class="cover-scene" role="img" aria-label="Photograph of an overcast evening sky over distant hazy hills, a dark treeline with a small chapel tower, and golden grass in the foreground"></div>
      <h1 class="title">
        <span class="title-line-one">Quiet</span>
        <span class="title-line-two">Lanterns</span>
      </h1>
      <p class="subtitle">Ways to Notice and Step Away From Harmful Circles While Keeping Steady Belief</p>
      <p class="author">Dorian T. Wexcombe</p>
    </section>
  </main>
</body>
</html>
```